Wohnhof am Weiher - Zeitungsinserat für den Verkauf von Eigentumswohnungen

Wir brauchen ein Zeitungsinserat in zwei Formaten. Einmal 296 Breite x 440 Höhe mm und einmal 296 Breite x 220 mm Höhe.
Als Basis dient der sehr grobe Entwurf im Powerpoint (Entwurf.pptx).
Auf dem Entwurf fehlen noch die Kontaktangeben:
Brunnhofer Liegenschaften AG
Seematteweg 14
4387 Tannried
079 462 37 58
rbrunnhofer@tessin-ostwald.ch

Zudem muss noch der Link auf die Webseite aufgeführt werden.
www.wohnhof-am-weiher.ch

Zudem fehlt noch der Text:
Fordern Sie noch heute die Verkaufsunterlagen gedruckt oder per Email an. Schreiben Sie uns einfach eine Chatpost mit Ihrer Adresse.

Ich habe noch Files von den Innenvisualisierungen, den Aussenvisualisierungen sowie unser Logo hinzugefügt. Zudem habe ich Ihnen die Verkaufsbrochure angefügt. Sie können die Daten vom Entwurf gerne ergänzen wenn Ihnen etwas gefällt. Schön wäre es, wenn Sie den Stil ähnlich machen würden wie die Brochure.

Target Market(s)

Famillien, Paare und Rentner

Font styles to use
Serif

Colors

Designer to choose colors to be used in the design.

Requirements
Must have
• Tolles Design das sofort anspricht!

```html
<!DOCTYPE html>
<html lang="de">
<head>
<meta charset="utf-8">
<title>Wohnhof am Weiher – Inserat</title>
<link href="https://fonts.googleapis.com/css2?family=Montserrat:ital,wght@0,300;0,400;0,600;0,800;0,900;1,800&display=swap" rel="stylesheet">
<style>
:root{
  --stage:#e5dbcf;
  --navy:#1f2e3d;
  --navy-soft:rgba(31,46,61,.93);
  --red:#e0151f;
  --blue:#2f6ea5;
  --white:#ffffff;
  --row:#d9d6d3;
  --row-alt:#ebe9e7;
  --ink:#2a2a2a;
  --tick:#8dc63f;
}
*{box-sizing:border-box;margin:0;padding:0}
html,body{width:1200px;height:800px;overflow:hidden;background:var(--stage);font-family:'Montserrat',sans-serif}
.ad{position:absolute;left:340px;top:14px;width:520px;height:772px;background:var(--white);overflow:hidden;box-shadow:0 6px 24px rgba(0,0,0,.18)}
.ad-shapes{position:absolute;inset:0}
.request-bar{position:absolute;left:0;top:0;width:100%;height:34px;background:var(--red);color:var(--white);font-size:7.6px;line-height:1.35;padding:8px 150px 0 22px;font-weight:400}
.brand{position:absolute;right:14px;top:8px;display:flex;align-items:center;gap:5px;color:var(--white);font-size:10px;font-weight:600;letter-spacing:.5px}
.brand-mark{width:7px;height:7px;background:var(--red)}
.headline{position:absolute;left:28px;top:58px;color:var(--white);text-transform:uppercase}
.headline-strong{font-weight:900;font-size:50px;line-height:1;letter-spacing:1px}
.headline-light{font-weight:300;font-size:48px;line-height:1.02;letter-spacing:2px}
.headline-sub{font-weight:400;font-size:15.5px;line-height:1.15;margin-top:10px;letter-spacing:.8px}
.perks{position:absolute;left:34px;top:236px;display:grid;grid-template-columns:150px 200px;gap:4px 14px;color:var(--white);font-size:12.5px;font-weight:300;letter-spacing:.6px}
.perks li{list-style:none;display:flex;align-items:flex-start;gap:8px;line-height:1.15}
.perks svg{flex:none;margin-top:1px}
.tables{position:absolute;left:12px;top:520px;width:496px;display:grid;grid-template-columns:repeat(3,minmax(0,1fr));gap:6px}
.house{min-width:0}
.house-title{background:var(--navy);color:var(--white);font-weight:800;font-style:italic;font-size:13px;text-align:center;padding:3px 0 2px;letter-spacing:.5px}
.unit{display:grid;grid-template-columns:28px 20px 20px minmax(0,1fr) 34px;gap:2px;padding:4px 4px;font-size:6px;line-height:1.2;color:var(--ink);background:var(--row)}
.unit:nth-child(odd){background:var(--row-alt)}
.unit .price{text-align:right;font-weight:600}
.contact-bar{position:absolute;left:0;bottom:0;width:100%;height:62px;background:var(--red);color:var(--white);font-size:10.5px;font-weight:400}
.contact-item{display:flex;align-items:center;gap:6px;line-height:1.2}
.contact-web{position:absolute;right:18px;top:8px;font-size:10.5px;display:flex;gap:6px;align-items:center}
.contact-row{position:absolute;left:18px;right:18px;bottom:8px;display:flex;justify-content:space-between;align-items:center}
</style>
</head>
<body>
<main class="ad">
  <svg class="ad-shapes" width="520" height="772" viewBox="0 0 520 772">
    <defs>
      <linearGradient id="exterior" x1="0" y1="0" x2="0" y2="1">
        <stop offset="0" stop-color="#c9d3d6"/>
        <stop offset=".45" stop-color="#8c9a8c"/>
        <stop offset="1" stop-color="#3f5a3a"/>
      </linearGradient>
      <linearGradient id="interior-a" x1="0" y1="0" x2="1" y2="1">
        <stop offset="0" stop-color="#d9d6cf"/><stop offset="1" stop-color="#6b6257"/>
      </linearGradient>
      <linearGradient id="interior-b" x1="0" y1="0" x2="1" y2="1">
        <stop offset="0" stop-color="#eceae6"/><stop offset="1" stop-color="#9a8565"/>
      </linearGradient>
      <linearGradient id="interior-c" x1="0" y1="0" x2="1" y2="1">
        <stop offset="0" stop-color="#f1efeb"/><stop offset="1" stop-color="#8a7a68"/>
      </linearGradient>
    </defs>
    <polygon points="230,34 520,34 520,300 330,500 200,500" fill="url(#exterior)" role="img" aria-label="Aussenvisualisierung der Wohnanlage mit Bäumen"/>
    <polygon points="0,34 395,34 330,190 170,520 0,520" fill="var(--navy-soft)"/>
    <polygon points="0,520 170,520 60,700 0,700" fill="var(--navy)"/>
    <polygon points="430,0 520,0 520,60" fill="var(--blue)"/>
    <g stroke="#fff" stroke-width="6" stroke-linejoin="round">
      <polygon points="70,405 140,345 250,360 190,435 90,430" fill="url(#interior-a)" role="img" aria-label="Innenvisualisierung Wohnzimmer mit Fensterfront"/>
      <polygon points="290,345 340,310 470,330 425,390 305,378" fill="url(#interior-b)" role="img" aria-label="Innenvisualisierung Küche mit Essbereich"/>
      <polygon points="230,465 272,405 370,410 345,490 250,500" fill="url(#interior-c)" role="img" aria-label="Innenvisualisierung Essbereich mit Pendelleuchte"/>
    </g>
  </svg>

  <p class="request-bar">Fordern Sie noch heute die Verkaufsunterlagen gedruckt oder per Email an.<br>Schreiben Sie uns einfach eine Chatpost mit Ihrer Adresse.</p>
  <div class="brand"><span class="brand-mark"></span>BRUNNHOFER</div>

  <header class="headline">
    <h1 class="headline-strong">Wohnhof</h1>
    <p class="headline-light">am Weiher</p>
    <p class="headline-sub">Hochwertige und moderne<br>Eigentumswohnungen</p>
  </header>

  <ul class="perks">
    <li><svg width="14" height="12" viewBox="0 0 14 12"><path d="M1 6l4 4 8-9" fill="none" stroke="var(--tick)" stroke-width="2.4"/></svg>Bus und Bahn</li>
    <li><svg width="14" height="12" viewBox="0 0 14 12"><path d="M1 6l4 4 8-9" fill="none" stroke="var(--tick)" stroke-width="2.4"/></svg>Einkaufen und weitere Dienstleistungen</li>
    <li><svg width="14" height="12" viewBox="0 0 14 12"><path d="M1 6l4 4 8-9" fill="none" stroke="var(--tick)" stroke-width="2.4"/></svg>Basel - Stadt</li>
    <li><svg width="14" height="12" viewBox="0 0 14 12"><path d="M1 6l4 4 8-9" fill="none" stroke="var(--tick)" stroke-width="2.4"/></svg>Erholung im Grünen</li>
    <li><svg width="14" height="12" viewBox="0 0 14 12"><path d="M1 6l4 4 8-9" fill="none" stroke="var(--tick)" stroke-width="2.4"/></svg>Autobahn</li>
  </ul>

  <section class="tables">
    <div class="house">
      <h2 class="house-title">HAUS A</h2>
      <div class="unit"><span>Attika</span><span>4.5 Zimmer</span><span>108m²</span><span>105m² Sonnenterrasse</span><span class="price">945'000 CHF</span></div>
      <div class="unit"><span>Ober&shy;geschoss</span><span>3.5 Zimmer</span><span>81m²</span><span>16m² Balkon</span><span class="price">754'800 CHF</span></div>
      <div class="unit"><span>Ober&shy;geschoss</span><span>4.5 Zimmer</span><span>102m²</span><span>33m² Balkon</span><span class="price">640'000 CHF</span></div>
      <div class="unit"><span>Erd&shy;geschoss</span><span>3.5 Zimmer</span><span>81m²</span><span>16m² gedeckter Sitzplatz &amp; eigener Garten</span><span class="price">657'000 CHF</span></div>
      <div class="unit"><span>Erd&shy;geschoss</span><span>4.5 Zimmer</span><span>102m²</span><span>33m² gedeckter Sitzplatz &amp; eigener Garten</span><span class="price">765'000 CHF</span></div>
    </div>
    <div class="house">
      <h2 class="house-title">HAUS B</h2>
      <div class="unit"><span>Attika</span><span>4.5 Zimmer</span><span>109m²</span><span>107m² Sonnenterrasse</span><span class="price">965'000 CHF</span></div>
      <div class="unit"><span>Ober&shy;geschoss</span><span>2.5 Zimmer</span><span>69m²</span><span>14m² Balkon</span><span class="price">550'000 CHF</span></div>
      <div class="unit"><span>Ober&shy;geschoss</span><span>4.5 Zimmer</span><span>117m²</span><span>42m² Balkon</span><span class="price">877'500 CHF</span></div>
      <div class="unit"><span>Erd&shy;geschoss</span><span>2.5 Zimmer</span><span>69m²</span><span>14m² gedeckter Sitzplatz &amp; eigener Garten</span><span class="price">560'000 CHF</span></div>
      <div class="unit"><span>Erd&shy;geschoss</span><span>4.5 Zimmer</span><span>117m²</span><span>42m² gedeckter Sitzplatz &amp; eigener Garten</span><span class="price">889'000 CHF</span></div>
    </div>
    <div class="house">
      <h2 class="house-title">HAUS C</h2>
      <div class="unit"><span>Attika</span><span>4.5 Zimmer</span><span>129m²</span><span>132m² Sonnenterrasse</span><span class="price">1'135'000 CHF</span></div>
      <div class="unit"><span>Ober&shy;geschoss</span><span>5.5 Zimmer</span><span>143m²</span><span>43m² Balkon</span><span class="price">1'058'000 CHF</span></div>
      <div class="unit"><span>Ober&shy;geschoss</span><span>3.5 Zimmer</span><span>96m²</span><span>23m² Balkon</span><span class="price">789'000 CHF</span></div>
      <div class="unit"><span>Erd&shy;geschoss</span><span>5.5 Zimmer</span><span>143m²</span><span>43m² gedeckter Sitzplatz &amp; eigener Garten</span><span class="price">1'065'000 CHF</span></div>
      <div class="unit"><span>Erd&shy;geschoss</span><span>3.5 Zimmer</span><span>96m²</span><span>23m² gedeckter Sitzplatz &amp; eigener Garten</span><span class="price">740'000 CHF</span></div>
    </div>
  </section>

  <footer class="contact-bar">
    <div class="contact-web">
      <svg width="13" height="13" viewBox="0 0 14 14"><circle cx="7" cy="7" r="6" fill="none" stroke="#fff" stroke-width="1.2"/><path d="M1 7h12M7 1c3 3 3 9 0 12M7 1c-3 3-3 9 0 12" fill="none" stroke="#fff" stroke-width="1"/></svg>
      www.wohnhof-am-weiher.ch
    </div>
    <div class="contact-row">
      <div class="contact-item">
        <svg width="12" height="15" viewBox="0 0 12 15"><path d="M6 14s5-5 5-8.5A5 5 0 0 0 1 5.5C1 9 6 14 6 14z" fill="none" stroke="#fff" stroke-width="1.3"/><circle cx="6" cy="5.5" r="1.8" fill="#fff"/></svg>
        <span>Seematteweg 14,<br>4387 Tannried</span>
      </div>
      <div class="contact-item">
        <svg width="13" height="13" viewBox="0 0 14 14"><path d="M3 1l2.5 3-1.5 1.5c1 2 2.5 3.5 4.5 4.5L10 8.5l3 2.5-1.5 2C6 13 1 8 1 2.5z" fill="none" stroke="#fff" stroke-width="1.2" stroke-linejoin="round"/></svg>
        <span>079 462 37 58</span>
      </div>
      <div class="contact-item">
        <svg width="14" height="11" viewBox="0 0 14 11"><rect x=".7" y=".7" width="12.6" height="9.6" fill="none" stroke="#fff" stroke-width="1.2"/><path d="M1 1l6 5 6-5" fill="none" stroke="#fff" stroke-width="1.2"/></svg>
        <span>rbrunnhofer@tessin-ostwald.ch</span>
      </div>
    </div>
  </footer>
</main>
</body>
</html>
```